Laboratory and geotechnical service provider needs Word template

We require a new Word Template for our business. We are looking for a modern, business-like format. We typically generate reports such as management plans, business plans, method statements, technical reports. These reports cover generally between 5 and 30 pages, but sometimes up to 500 pages including the appendices.

Lab reports have their own formats and are not parts of this scope.

Target Market(s)

We report to Clients such as construction industry contractors, governmental departments and engineering consultants.

Industry/Entity Type

Technical Service

Colors

Designer to choose colors to be used in the design.

Requirements
Must have
• The report needs a fancy cover page with a title field, subtitle, project field, client name field, reference number field. Photo/graphics as background on cover. Second page needs a revision table for document control. Table of contents up to 2 levels. Appendices to be part of TOC. Report first page with custom headings for body text, titles, subtitles, headings 1, 2, 3, etc. Include a table with caption, figure with caption, bullet list, numbered list. Appendix page. Please use fonts consistently, choose a common, but professional, modern font.
Nice to have
• We traditionally use black and yellow as company colours. Please visit our company page www.harbentestworks.com.
Should not have
• The two attached word documents is what we use now for your information, we are looking for something better!

```html
<!DOCTYPE html>
<html lang="en">
<head>
<meta charset="utf-8">
<title>Harben Testworks – Report Template Pages</title>
<link rel="stylesheet" href="https://fonts.googleapis.com/css2?family=Open+Sans:ital,wght@0,400;0,600;0,700;1,400&display=swap">
<style>
:root{
  --canvas:#d9d9d9;
  --paper:#ffffff;
  --yellow:#f7ee3b;
  --logo-yellow:#fff200;
  --black:#141414;
  --ink:#2b2b2b;
  --grey:#6d6d6d;
  --rule:#9a9a9a;
  --blue:#2a5ca8;
  --row-blue:#cfe8f3;
  --row-grey:#d6d6d6;
  --head-grey:#7d7d7d;
  --olive:#a9ae8a;
  --red:#b0182c;
  --photo-a:#8a8f98;
  --photo-b:#c9cdd4;
}
*{margin:0;padding:0;box-sizing:border-box}
html,body{width:1200px;height:1022px;overflow:hidden;background:var(--canvas)}
body{position:relative;font-family:"Open Sans",Arial,sans-serif;color:var(--ink)}
.page{position:absolute;width:245px;height:346px;background:var(--paper);overflow:hidden;box-shadow:0 1px 3px rgba(0,0,0,.12)}
.corner-wedge{position:absolute;top:0;right:0}
.page-head{position:absolute;left:0;top:20px;display:flex;align-items:center;gap:4px}
.page-head .bar{width:13px;height:5px;background:var(--black)}
.page-head h1{font-size:6.8px;font-weight:400;letter-spacing:.1px;color:var(--black)}
.page-foot{position:absolute;left:0;bottom:0;width:245px;height:30px}
.foot-mark{position:absolute;left:18px;top:7px;display:flex;align-items:center;gap:2px;font-size:5.4px;font-weight:700;line-height:1;color:var(--black)}
.foot-mark .dot{width:5px;height:5px;background:var(--black)}
.foot-mark span{width:22px}
.page-num{position:absolute;right:6px;top:17px;font-size:3px;color:#fff}
.body-text{font-size:3.1px;line-height:5.2px;color:var(--ink)}
.body-text p{margin-bottom:3px}
.h2{font-size:6px;color:var(--black);font-weight:600;margin:5px 0 2px}
.h3{font-size:4.4px;font-style:italic;color:var(--grey);margin:3px 0 1px}
.link{color:var(--blue)}
.accent-red{color:var(--red)}
.photo{position:absolute;background:linear-gradient(135deg,var(--photo-b),var(--photo-a))}
/* cover */
.cover{background:var(--yellow)}
.cover-brand{position:absolute;left:86px;top:12px;width:72px;height:52px;background:var(--logo-yellow);display:flex;flex-direction:column;justify-content:center;align-items:center;gap:3px}
.cover-brand .sq{width:7px;height:7px;background:var(--black)}
.cover-brand span{font-size:7.6px;font-weight:700;color:var(--black);line-height:1.05;text-align:center}
.cover-band{position:absolute;left:0;top:77px;width:245px;height:10px;background:var(--black);color:#fff;font-size:8px;font-weight:700;text-align:center;line-height:10px;letter-spacing:.2px}
.cover-sub{position:absolute;left:0;top:92px;width:245px;text-align:center;font-size:4.8px;color:var(--black)}
.cover-fields{position:absolute;left:130px;top:113px;font-size:3.4px;line-height:4px;color:var(--black)}
.cover-fields dt{font-weight:700;margin-top:6px}
.cover-fields dt:first-child{margin-top:0}
.cover-foot{position:absolute;left:0;top:294px;width:245px;height:52px;background:var(--black)}
.cover-contact{position:absolute;left:100px;top:17px;border-left:1.5px solid #fff;padding-left:3px;font-size:3.2px;line-height:4.6px;color:#fff}
.cover-contact b{font-weight:700}
/* toc */
.toc{position:absolute;left:18px;top:46px;width:212px}
.toc h2{font-size:6px;font-weight:600;color:var(--black);margin-bottom:6px}
.toc-row{display:flex;align-items:baseline;font-size:3.1px;line-height:5px;color:var(--ink)}
.toc-row .fill{flex:1;border-bottom:.4px dotted var(--grey);margin:0 2px}
.toc-row.l1{font-weight:700}
.toc-row.l2{padding-left:5px}
.toc-row.l3{padding-left:10px}
/* tables */
.data-table{border-collapse:separate;border-spacing:1px 1.2px;font-size:2.7px;width:100%}
.data-table th{background:var(--head-grey);color:#fff;font-weight:400;height:5px;text-align:center}
.data-table td{background:var(--row-blue);height:5px;padding:0 3px}
.data-table td.num{text-align:center}
.data-table tr.phase td{color:var(--blue);font-weight:600;font-size:3px}
.data-table tr.total td{background:var(--row-grey);font-weight:700}
.data-table tr.grand td{background:var(--head-grey);color:#fff;font-weight:700}
.stripe-block{position:absolute;left:20px;width:196px}
.stripe-block div{height:6px;background:var(--row-blue);margin-bottom:6px;border-top:.5px solid #9cc7e2}
</style>
</head>
<body>

<!-- Cover -->
<section class="page cover" style="left:60px;top:116px">
  <div class="cover-brand"><i class="sq"></i><span>HARBEN<br>TESTWORKS</span></div>
  <div class="cover-band">XYZ SERVICE REPORT</div>
  <div class="cover-sub">SUBTITLE TEXT HERE SUBTITLE TEXT HERE</div>
  <svg width="245" height="346" style="position:absolute;left:0;top:0" aria-hidden="false">
    <defs>
      <linearGradient id="drill" x1="0" y1="0" x2="1" y2="1"><stop offset="0" stop-color="#b9c6d3"/><stop offset=".6" stop-color="#c9a57a"/><stop offset="1" stop-color="#9c7c58"/></linearGradient>
      <linearGradient id="lab" x1="0" y1="0" x2="1" y2="1"><stop offset="0" stop-color="#d8dde3"/><stop offset="1" stop-color="#7d8894"/></linearGradient>
    </defs>
    <polygon points="45,104 92,151 45,198 -2,151" fill="url(#drill)" role="img" aria-label="Photo of a drilling rig on a desert site"/>
    <polygon points="20,200 55,235 20,270 -15,235" fill="var(--black)"/>
    <polygon points="95,186 133,224 95,262 57,224" fill="var(--black)" rx="4"/>
    <polygon points="48,252 90,294 48,336 6,294" fill="url(#lab)" role="img" aria-label="Photo of technicians working in a laboratory"/>
  </svg>
  <dl class="cover-fields">
    <dt>PROJECT DETAIL:</dt><dd>XYZ</dd>
    <dt>CLIENT DETAIL:</dt><dd>00/00 Marlow Street<br>Kelvin Grove<br>City Name XXXX<br>Australia<br>T: 0400 000 000<br>E: info@northvane.com</dd>
    <dt>REF#:</dt><dd>XXXXXXXXXXXXX</dd>
    <dt>DATE:</dt><dd>06-12-2019</dd>
  </dl>
  <div class="cover-foot">
    <div class="cover-contact">Harben Testworks Co. WLL<br><b>TEL:</b> (+974) 4000 1100, 4000 1101 | <b>FAX:</b> (+974) 4000 1199<br>P.O. BOX 0000, DOHA, QATAR | E: office@harbentestworks.com</div>
  </div>
</section>

<!-- Table of contents -->
<section class="page" style="left:334px;top:116px">
  <svg class="corner-wedge" width="130" height="14"><polygon points="0,0 130,0 130,12" fill="var(--yellow)"/></svg>
  <header class="page-head"><i class="bar"></i><h1>TABLE OF CONTENTS</h1></header>
  <nav class="toc">
    <h2>Contents</h2>
    <div class="toc-row l1">1. Table of Contents<i class="fill"></i>01</div>
    <div class="toc-row l2">1.1. Executive Summary<i class="fill"></i>02</div>
    <div class="toc-row l3">1.1.1. Our Understanding of Your Needs<i class="fill"></i>02</div>
    <div class="toc-row l1">2. Our Recommendations<i class="fill"></i>03</div>
    <div class="toc-row l2">2.1. Our Approach<i class="fill"></i>05</div>
    <div class="toc-row l3">2.1.1. Budget and Timeframe<i class="fill"></i>07</div>
    <div class="toc-row">3. Appendix A: About Selwyn Ridge<i class="fill"></i>10</div>
    <div class="toc-row l2">3.1. Appendix B: Selected Client List<i class="fill"></i>10</div>
    <div class="toc-row l3">3.1.1. Appendix C: Our Capabilities<i class="fill"></i>11</div>
    <div class="toc-row">Appendix D: Our Process<i class="fill"></i>12</div>
  </nav>
  <footer class="page-foot">
    <svg width="245" height="30" style="position:absolute;left:0;top:0"><rect x="44" y="14" width="176" height="1.6" fill="var(--black)"/><polygon points="200,14 222,14 226,20 206,20" fill="var(--yellow)"/><polygon points="212,16 245,16 245,23 218,23" fill="var(--black)"/></svg>
    <div class="foot-mark"><i class="dot"></i><span>HARBEN TESTWORKS</span></div>
  </footer>
</section>

<!-- Executive summary -->
<section class="page" style="left:608px;top:116px">
  <svg class="corner-wedge" width="130" height="14"><polygon points="0,0 130,0 130,12" fill="var(--yellow)"/></svg>
  <header class="page-head"><i class="bar"></i><h1>EXECUTIVE SUMMARY</h1></header>
  <div class="body-text" style="position:absolute;left:16px;top:40px;width:210px">
    <div class="h2">1&nbsp; Solution</div>
    <div style="padding-left:9px">
      <div class="h3" style="font-size:3.4px">AI automated accounting</div>
      <p>Tallyra builds automation in stages on top of its current system to reach full automation. It starts by connecting to all sources of accounting data such as bank accounts, credit cards, webshops or document management systems. Based on these data, Tallyra AI creates bookings and generates financial reports. Finally, Tallyra AI features a chat-like interface that allows users to communicate seamlessly with it, viewing it as a trusted advisor over time for all their accounting queries.</p>
      <div class="h3" style="font-size:3.4px">1.1&nbsp; Blockchain software license or Token-as-a-License (TaaL)</div>
      <p>It is possible to create tokens on blockchain that represent software licenses, also known as Token-as-a-Licence (TaaL). Tallyra creates TaaL by using the Corvex official wallet which interacts with the Corvex blockchain. Upon purchase of TaaL, the token holder is free to transfer or sell TaaL using the secondary market that is built directly over the blockchain, in our case the Corvex marketplace. Tallyra checks the validity of a token against the blockchain ensuring that token holders have access to the software. TaaL make distribution and securisation of software licenses easier for software developers. It also makes the management and resale of software license easier for software owners. All in all, TaaL has a higher value as a normal software license.</p>
    </div>
    <div class="h2" style="font-size:5.4px">2.&nbsp; Pre-ICO Token sale</div>
    <div style="padding-left:9px">
      <p>To realize this innovative vision, Tallyra is launching a pre-ICO in form of a token sale on Corvex blockchain. 20,000,000 tokens are available to purchase for the price of CHF 0.10 each during a 30-day period to be announced. Tokens represent Tallyra lifelong software licenses and by purchasing enough tokens, holders gain access to Tallyra software. 15,000 tokens give access to Tallyra invoicing or accounting. 20,000 tokens give access to both Tallyra accounting and invoicing. Future customers will still have the opportunity to buy directly yearly or monthly subscriptions to have access to Tallyra.</p>
      <div class="h2" style="font-size:5px">Future plans</div>
      <p>A future ICO is planned between 18 and 24 months after the pre-ICO token sale. This offering will support the development of Tallyra into a fully decentralized, privacy-focused ecosystem of applications. The new model will reward each participant so that a new world with zero administrative tasks becomes reality.</p>
    </div>
  </div>
  <footer class="page-foot">
    <svg width="245" height="30" style="position:absolute;left:0;top:0"><rect x="44" y="14" width="176" height="1.6" fill="var(--black)"/><polygon points="200,14 222,14 226,20 206,20" fill="var(--yellow)"/><polygon points="212,16 245,16 245,23 218,23" fill="var(--black)"/></svg>
    <div class="foot-mark"><i class="dot"></i><span>HARBEN TESTWORKS</span></div>
    <div class="page-num">1</div>
  </footer>
</section>

<!-- Headline page, two photos -->
<section class="page" style="left:882px;top:116px">
  <svg class="corner-wedge" width="130" height="14"><polygon points="0,0 130,0 130,12" fill="var(--yellow)"/></svg>
  <header class="page-head"><i class="bar"></i><h1>HEADLINE HERE</h1></header>
  <div class="photo" style="left:20px;top:36px;width:87px;height:130px" role="img" aria-label="Photo of a hand drawing a cloud computing sketch"></div>
  <div class="photo" style="left:20px;top:186px;width:87px;height:116px" role="img" aria-label="Photo of a businessman in a suit with a cloud sketch"></div>
  <div class="body-text" style="position:absolute;left:118px;top:38px;width:110px">
    <p style="font-size:4.8px;line-height:5.2px;color:var(--olive);font-weight:600">Tallyra's mission is to help and support the self-employed and small business owners with their administrative tasks so they can focus on what matters — their business.</p>
    <p>Administrative tasks are cumbersome, time-consuming and often prevent small owners from focusing their time and energy on their business and their customers. They can also be extremely stressful and nerve-wracking for those attempting these tasks for the first time.</p>
    <p>At Tallyra, we envisage accounting for the self-employed and small business owners as being <span class="link">automated and decentralized</span></p>
    <p>Accounting can and should be done automatically. By connecting to all sources of accounting data such as bank accounts, payment systems, e-commerce websites, and invoicing systems, Tallyra AI automatically completes these tasks, which would take hours to do manually. Bookings are created automatically and fully completed. Financial statements are available within a couple of clicks, and after analysing your data, Tallyra AI will offer you tips to improve your financial stability.</p>
    <p>What may seem like a pipedream to the millions of self-employed who struggle with</p>
    <div class="h2" style="font-size:5.2px;margin-top:6px">The Tallyra model</div>
    <p>Tallyra is based on an innovative license model that uses Token-as-a-License (TaaL). The token represents lifelong software license for Tallyra solutions. The Pre-ICO token sales will enable Tallyra to complete its development of Tallyra AI to deliver fully automatic bookkeeping.</p>
    <p style="margin-top:10px">launch accounting on the blockchain and ensure your</p>
  </div>
  <footer class="page-foot">
    <svg width="245" height="30" style="position:absolute;left:0;top:0"><rect x="44" y="14" width="176" height="1.6" fill="var(--black)"/><polygon points="200,14 222,14 226,20 206,20" fill="var(--yellow)"/><polygon points="212,16 245,16 245,23 218,23" fill="var(--black)"/></svg>
    <div class="foot-mark"><i class="dot"></i><span>HARBEN TESTWORKS</span></div>
    <div class="page-num">5</div>
  </footer>
</section>

<!-- Headline page, single photo -->
<section class="page" style="left:62px;top:506px">
  <svg class="corner-wedge" width="130" height="14"><polygon points="0,0 130,0 130,12" fill="var(--yellow)"/></svg>
  <header class="page-head"><i class="bar"></i><h1>HEADLINE HERE</h1></header>
  <div class="photo" style="left:18px;top:35px;width:197px;height:88px" role="img" aria-label="Photo of a businessman sketching a cloud network diagram"></div>
  <div class="body-text" style="position:absolute;left:18px;top:128px;width:200px">
    <p style="font-size:5px;line-height:5.6px;font-weight:700;color:var(--black)">Tallyra's mission is to help and support the self-employed and small business owners with</p>
    <p>Administrative tasks are cumbersome, time-consuming and often prevent small owners from focusing their time and energy on their business and their customers. They can also be extremely stressful and nerve-wracking for those attempting these tasks for the first time.</p>
    <p>At Tallyra, we envisage accounting for the self-employed and small business owners as being <br><span class="link">automated and decentralized</span></p>
  </div>
  <div class="stripe-block" style="top:202px"><div></div><div></div><div></div><div></div></div>
  <div class="body-text" style="position:absolute;left:18px;top:268px;width:200px">
    <p>Tallyra is based on an innovative license model that uses Token-as-a-License (TaaL). The token represents lifelong software license for Tallyra solutions. The Pre-ICO token sales will enable Tallyra to complete its development of Tallyra AI to deliver fully automatic bookkeeping.</p>
    <p>with leading edge business data access to ensure you have the best available data at your fingertips.</p>
  </div>
  <footer class="page-foot">
    <svg width="245" height="30" style="position:absolute;left:0;top:0"><rect x="44" y="14" width="176" height="1.6" fill="var(--black)"/><polygon points="200,14 222,14 226,20 206,20" fill="var(--yellow)"/><polygon points="212,16 245,16 245,23 218,23" fill="var(--black)"/></svg>
    <div class="foot-mark"><i class="dot"></i><span>HARBEN TESTWORKS</span></div>
    <div class="page-num">4</div>
  </footer>
</section>

<!-- Budget and timeframe -->
<section class="page" style="left:334px;top:506px">
  <svg class="corner-wedge" width="130" height="14"><polygon points="0,0 130,0 130,12" fill="var(--yellow)"/></svg>
  <header class="page-head"><i class="bar"></i><h1>BUDGET AND TIMEFRAME</h1></header>
  <div class="body-text" style="position:absolute;left:20px;top:32px;width:196px">
    <div class="h2" style="font-size:5.6px;margin-top:0">Implementation Estimate</div>
    <p>The bulk of the implementation costs will be defined by discovery. Based on similar CRM implementation projects, we feel expect that the CRM side will be somewhere between 200 and 300 hours, give or take. The wide swing in hours in phase Phase 1 is related currently to the ill-under-defined nature of both the integration needs and our role in the integration project. Our focus in discovery (as mentioned above) will be to nail down and finalize those requirements and our role as it relates to what is needed to integrate the sites with the CRM.</p>
    <table class="data-table" style="margin-top:6px">
      <tr><th style="width:52%">Task</th><th style="width:20%">Hours</th><th>Cost</th></tr>
      <tr><td>Discovery</td><td class="num">40</td><td class="num">$8,000</td></tr>
      <tr class="phase"><td>Phase 1</td><td></td><td></td></tr>
      <tr><td>Discovery</td><td class="num">20-40</td><td class="num">$8,000</td></tr>
      <tr><td>Discovery</td><td class="num">20-40</td><td class="num">$8,000</td></tr>
      <tr><td>Discovery</td><td class="num">20-40</td><td class="num">$8,000</td></tr>
      <tr class="total"><td>Total Phase 1</td><td class="num">80-240</td><td class="num">$16,800-40,000</td></tr>
      <tr class="phase"><td>Phase 2</td><td></td><td></td></tr>
      <tr><td>Discovery</td><td class="num">20-40</td><td class="num">$8,000</td></tr>
      <tr class="total"><td>Total Phase 2</td><td class="num">80-240</td><td class="num">$16,800-40,000</td></tr>
      <tr class="grand"><td>Total Estimated Implementation Cost</td><td class="num">220-480</td><td class="num">$44,000-96,000</td></tr>
    </table>
    <div class="h2" style="font-size:5.6px;margin-top:8px">Project Timeline</div>
    <p>Based on the information we have out our disposal, the March 21st launch date doesn't seem a realistic goal to get both the work done needed to provide the foundation for the future CRM instance and the integration given the state of apparent flux of the requirements. That said, we feel it prudent to proceed with discovery before committing to or pushing that date. We are currently estimating that the first phase will take somewhere between 7 and 12 weeks (including discovery) to complete.</p>
    <table class="data-table" style="margin-top:5px">
      <tr><th style="width:62%">Task</th><th>Weeks to Complete</th></tr>
      <tr><td>Discovery</td><td class="num">1-2</td></tr>
      <tr><td>Phase 1</td><td class="num">6-10</td></tr>
      <tr><td>Phase 2</td><td class="num">8-12</td></tr>
      <tr class="total"><td>Total Number of Weeks</td><td></td></tr>
    </table>
  </div>
  <footer class="page-foot">
    <svg width="245" height="30" style="position:absolute;left:0;top:0"><rect x="44" y="14" width="176" height="1.6" fill="var(--black)"/><polygon points="200,14 222,14 226,20 206,20" fill="var(--yellow)"/><polygon points="212,16 245,16 245,23 218,23" fill="var(--black)"/></svg>
    <div class="foot-mark"><i class="dot"></i><span>HARBEN TESTWORKS</span></div>
    <div class="page-num">3</div>
  </footer>
</section>

<!-- Vision -->
<section class="page" style="left:608px;top:506px">
  <svg class="corner-wedge" width="130" height="14"><polygon points="0,0 130,0 130,12" fill="var(--yellow)"/></svg>
  <header class="page-head"><i class="bar"></i><h1>VISION</h1></header>
  <div class="body-text" style="position:absolute;left:17px;top:33px;width:206px">
    <p>Administrative tasks are cumbersome, time-consuming and often prevent small owners from focusing their time and energy on their business and their customers. They can also be extremely stressful and nerve-wracking for those attempting these tasks for the first time.</p>
    <p style="text-align:center">At Tallyra, we envisage accounting for the self-employed and small business owners as being<br><span class="accent-red">automated and decentralized</span></p>
    <p>Accounting can and should be done automatically. By connecting to all sources of accounting data such as bank accounts, payment systems, e-commerce websites, and invoicing systems, Tallyra AI automatically completes these tasks, which would take hours to do manually. Bookings are created automatically and fully completed. Financial statements are available within a couple of clicks, and after analysing your data, Tallyra AI will offer you tips to improve your financial stability.</p>
    <p>What may seem like a pipedream to the millions of self-employed who struggle with their admin, is already a reality. Now is the time to join Tallyra on its mission to transform the world of bookkeeping through the power of AI.</p>
    <div class="h2" style="font-size:5.4px">The Tallyra model</div>
    <p>Tallyra is based on an innovative license model that uses Token-as-a-License (TaaL). The token represents lifelong software license for Tallyra solutions. The Pre-ICO token sales will enable Tallyra to complete its development of Tallyra AI to deliver fully automatic bookkeeping.</p>
    <p>The Pre-ICO token sale will also pave the way for a future Tallyra ICO. Tallyra will launch accounting on the blockchain and ensure your accounting data is comprehensive and private, but available everywhere within your preferred apps. It will empower you to manage your data as you see fit in a fully decentralized way.<br>Furthermore, a new range of business apps will connect to Tallyra to provide you</p>
    <p>with leading edge business data access to ensure you have the best available data at your fingertips.</p>
    <p>Tallyra supports strong data ownership laws that truly protect individuals and ensure they have complete ownership of their data. Through decentralization Tallyra helps to ensure you always have full ownership of your data to decide how it should be used.</p>
    <p>To find out more about the Tallyra AI project, and the Tallyra TaaL or if you are interested in purchasing Tallyra TaaL, please register with your email at <span class="link" style="text-decoration:underline">https://www.tallyra.example/ico</span> so we can notify you about our upcoming purchase periods.</p>
  </div>
  <footer class="page-foot">
    <svg width="245" height="30" style="position:absolute;left:0;top:0"><rect x="44" y="14" width="176" height="1.6" fill="var(--black)"/><polygon points="200,14 222,14 226,20 206,20" fill="var(--yellow)"/><polygon points="212,16 245,16 245,23 218,23" fill="var(--black)"/></svg>
    <div class="foot-mark"><i class="dot"></i><span>HARBEN TESTWORKS</span></div>
    <div class="page-num">1</div>
  </footer>
</section>

</body>
</html>
```